Brackenfold Builders

We are a General building contractor who specialises in building extensions, loft conversions, basement conversions, and general property refurbishment. The design should promote our company strap line On time-On budget-guaranteed. The design should also promote a confident and secure feeling as negotiating or contacting a builder can be a daunting task for most people who have not had any previous work. We have 30yrs experience within the industry. We intend to promote a VAT free offer.

```html
<!DOCTYPE html>
<html lang="en">
<head>
<meta charset="utf-8">
<title>Brackenfold Builders – Flyer</title>
<link rel="stylesheet" href="https://fonts.googleapis.com/css2?family=Oswald:wght@600&family=Bebas+Neue&family=Questrial&family=Lato:wght@400;700;900&display=swap">
<style>
  :root {
    --forest: #4f5b47;
    --forest-dark: #3b4536;
    --olive: #b9ab57;
    --olive-band: #bfb15e;
    --cream: #e4dda3;
    --ink: #1d1d1d;
    --body: #444;
    --white: #ffffff;
  }
  * { margin: 0; padding: 0; box-sizing: border-box; }
  html, body { width: 917px; height: 1200px; overflow: hidden; background: var(--white); }
  .flyer { position: relative; width: 917px; height: 1200px; overflow: hidden; background: var(--white); font-family: "Lato", sans-serif; }

  .header { position: absolute; left: 0; top: 0; width: 917px; height: 400px;
    background: linear-gradient(180deg, #5d6a55 0%, var(--forest) 45%, var(--forest-dark) 100%); }
  .header-zigzag { position: absolute; left: 0; top: 372px; width: 917px; height: 30px; }

  .photo-frame { position: absolute; background: var(--cream); padding: 9px; box-shadow: 0 4px 10px rgba(0,0,0,.35); }
  .photo-frame .photo { width: 100%; height: 100%; }
  .frame-site { left: 27px; top: 112px; width: 194px; height: 196px; }
  .frame-site .photo { background: linear-gradient(180deg, #7d6e5c 0%, #b7b4ad 50%, #b88a63 100%); }
  .frame-house { left: 216px; top: 74px; width: 468px; height: 264px; z-index: 2; }
  .frame-house .photo { background: linear-gradient(180deg, #dcdfe2 0%, #e8e4dc 45%, #6b6f5c 80%, #4d5a3f 100%); }
  .frame-flats { left: 682px; top: 106px; width: 194px; height: 200px; }
  .frame-flats .photo { background: linear-gradient(180deg, #e6e8ea 0%, #9b5a45 35%, #8b4c3a 100%); }

  .headline { position: absolute; top: 426px; left: 0; width: 917px; text-align: center;
    font-family: "Oswald", sans-serif; font-weight: 600; font-size: 45px; letter-spacing: 0.5px; color: var(--olive); line-height: 1; }
  .services { position: absolute; top: 482px; left: 0; width: 917px; text-align: center;
    font-family: "Lato", sans-serif; font-weight: 900; font-size: 20px; line-height: 24px; color: var(--ink); text-transform: uppercase; }

  .offer-ribbon { position: absolute; left: 50px; top: 552px; width: 817px; height: 62px; }
  .offer-text { position: absolute; left: 0; top: 552px; width: 917px; height: 62px; line-height: 64px; text-align: center;
    font-family: "Bebas Neue", sans-serif; font-size: 50px; color: var(--white); letter-spacing: 0.5px; }

  .strapline { position: absolute; top: 636px; left: 0; width: 917px; text-align: center;
    font-family: "Questrial", sans-serif; font-size: 27px; color: var(--ink); line-height: 34px; }
  .strapline .accent { color: var(--olive); }

  .intro { position: absolute; top: 722px; left: 30px; width: 857px; text-align: center;
    font-size: 14.4px; line-height: 19.6px; color: var(--body); }
  .detail { position: absolute; top: 863px; left: 330px; width: 240px; text-align: center;
    font-size: 14.4px; line-height: 19.6px; color: var(--body); }

  .footer-band { position: absolute; left: 0; top: 1020px; width: 917px; height: 180px; }

  .logo-house { position: absolute; left: 27px; top: 908px; width: 282px; height: 292px; }
  .logo-card { position: absolute; left: 37px; top: 978px; width: 263px; height: 145px; background: var(--white);
    display: flex; flex-direction: column; align-items: center; justify-content: center; gap: 12px; }
  .logo-name { display: flex; align-items: center; gap: 9px; font-family: "Lato", sans-serif; font-weight: 700; font-size: 19px; color: var(--forest); }
  .logo-mark { width: 14px; height: 14px; background: var(--olive); }
  .logo-tagline { font-size: 15px; color: var(--ink); }

  .contact { position: absolute; left: 27px; top: 1141px; display: flex; align-items: center; gap: 14px;
    font-weight: 700; font-size: 23px; color: var(--white); }
  .contact-item { display: flex; align-items: center; gap: 7px; }
  .contact svg { display: block; }

  .couple-photo { position: absolute; left: 560px; top: 928px; width: 357px; height: 272px;
    border-radius: 120px 0 0 0; border: 5px solid var(--white); border-right: 0; border-bottom: 0;
    background: linear-gradient(160deg, #c9a98c 0%, #7fb04a 35%, #4d6f94 70%, #2d3f55 100%); }
</style>
</head>
<body>
<div class="flyer">

  <header class="header" role="img" aria-label="Faded photograph of a large house behind the project photos"></header>
  <svg class="header-zigzag" viewBox="0 0 917 30" preserveAspectRatio="none" aria-hidden="true">
    <polygon fill="#ffffff" points="0,30 0,20 25,4 50,20 75,4 100,20 125,4 150,20 175,4 200,20 225,4 250,20 275,4 300,20 325,4 350,20 375,4 400,20 425,4 450,20 475,4 500,20 525,4 550,20 575,4 600,20 625,4 650,20 675,4 700,20 725,4 750,20 775,4 800,20 825,4 850,20 875,4 900,20 917,10 917,30"/>
  </svg>

  <div class="photo-frame frame-site"><div class="photo" role="img" aria-label="Photo of a building site with new block foundations"></div></div>
  <div class="photo-frame frame-house"><div class="photo" role="img" aria-label="Photo of a refurbished white Tudor-style house with an oak porch"></div></div>
  <div class="photo-frame frame-flats"><div class="photo" role="img" aria-label="Photo of a new red-brick block of flats"></div></div>

  <h1 class="headline">WE ARE A GENERAL BUILDING CONTRACTOR</h1>
  <p class="services">Who specialises in building extensions, loft conversions,<br>basement conversions, and general property refurbishment.</p>

  <svg class="offer-ribbon" viewBox="0 0 817 62" aria-hidden="true">
    <polygon fill="#b5a85a" points="0,0 817,0 795,31 817,62 0,62 22,31"/>
    <circle cx="44" cy="31" r="7" fill="#ffffff"/>
    <circle cx="773" cy="31" r="7" fill="#ffffff"/>
  </svg>
  <p class="offer-text">WE INTEND TO PROMOTE A VAT FREE OFFER</p>

  <p class="strapline">Our company strap line <span class="accent">On time-On budget-guaranteed.</span><br>We have 30yrs experience within the industry.</p>

  <p class="intro">Lorem Ipsum is simply dummy text of the printing and typesetting industry. Lorem Ipsum has been the industry's standard dummy text ever since the 1500s, when an unknown printer took a galley of type and scrambled it to make a type specimen book. It has survived not only five centuries, but also the leap into electronic typesetting, remaining essentially unchanged. It was popularised in the 1960s with the release of Letraset sheets containing Lorem Ipsum passages, and more recently with desktop publishing software like Aldus PageMaker including versions of Lorem Ipsum.</p>

  <p class="detail">Lorem Ipsum is simply dummy text of the printing and typesetting industry. em Ipsum.Lorem Ipsum has been the industry's standard dummy text ever since the 1500s, when an unknown printer took a galley of type and scrambled it.</p>

  <svg class="footer-band" viewBox="0 0 917 180" preserveAspectRatio="none" aria-hidden="true">
    <polygon fill="#bfb15e" points="0,180 0,14 280,14 300,30 325,10 350,30 375,10 400,30 425,10 450,30 475,10 500,30 525,10 550,30 575,10 600,30 625,10 650,30 675,10 700,30 725,10 750,30 775,10 800,30 825,10 850,30 875,10 900,30 917,18 917,180"/>
  </svg>

  <svg class="logo-house" viewBox="0 0 282 292" aria-hidden="true">
    <polygon fill="#bfb15e" points="0,70 141,0 282,70 282,292 0,292"/>
  </svg>
  <div class="logo-card">
    <div class="logo-name"><span class="logo-mark"></span>Brackenfold Builders</div>
    <div class="logo-tagline">On time On budget Guaranteed</div>
  </div>

  <div class="contact">
    <span class="contact-item">
      <svg width="24" height="16" viewBox="0 0 24 16" aria-hidden="true"><rect x="0" y="0" width="24" height="16" fill="#ffffff"/><polyline points="1,1 12,9 23,1" fill="none" stroke="#bfb15e" stroke-width="2"/></svg>
      www.brackenfold.example
    </span>
    <span class="contact-item">
      <svg width="18" height="20" viewBox="0 0 18 20" aria-hidden="true"><rect x="0" y="0" width="18" height="20" rx="4" fill="#ffffff"/><path d="M5 4 L8 4 L9 7 L7.5 8.5 C8.3 10.3 9.7 11.7 11.5 12.5 L13 11 L16 12 L16 15 C10 16 3 9 5 4 Z" fill="#bfb15e"/></svg>
      123-555-0198
    </span>
  </div>

  <div class="couple-photo" role="img" aria-label="Photo of a smiling couple sitting together on the floor of their new home"></div>

</div>
</body>
</html>
```